Quick Straightforward Billboard Redesign

- Design billboard sized for 10 foot' x 36' foot width live area size and please include bleeds 6" around all sides
- Exact blue color match is imperative in headline, logo, phone number bubble or wherever used. C-83 / M-45 / Y-1 / K-0-
- What I hope to illustrate is that our company offers the best porch screening in the area area, in regards to quality, expertise, durability, storms proof, but we do not build screen porches.
- Current board is attached below from previous designer, and as you can see sizing was off, white space on edges make it appear to be sized incorrectly.
- I also attached my own little mock up idea well well if it helps, favorite image, logo, headline, etc and ideas perhaps on expanding or making this better?

Thanks so much!

Target Market(s)

Drivers and passengers, Southeastern NC, are of immense new construction and high end homes.

Industry/Entity Type

Construction

Colors
0054AA
0677BA
7BADD7
CADEEF
E8F1F8

Requirements
Must have
• Blue color matching
Nice to have
• Design spins or other thoughts on my little mock up

```html
<!DOCTYPE html>
<html lang="en">
<head>
<meta charset="UTF-8">
<title>Harborline Screens Billboard</title>
<link href="https://fonts.googleapis.com/css2?family=Anton&family=Oswald:wght@500&family=Montserrat:wght@700&display=swap" rel="stylesheet">
<style>
  :root {
    --stage: #b1b1b1;
    --board: #ffffff;
    --brand-blue: #0677BA;
    --deep-blue: #0054AA;
    --headline-green: #5bbd5f;
    --accent-green: #27b463;
    --sky: #bcd9ee;
    --patio: #e9e4dc;
    --wicker: #6d6258;
  }
  * { box-sizing: border-box; margin: 0; padding: 0; }
  html, body {
    width: 1200px;
    height: 449px;
    overflow: hidden;
    background: var(--stage);
  }
  .billboard {
    position: absolute;
    left: 0;
    top: 58px;
    width: 1200px;
    height: 333px;
    background: var(--board);
    overflow: hidden;
  }
  .accent-bar {
    position: absolute;
    right: 0;
    top: 0;
    width: 115px;
    height: 100%;
    background: var(--accent-green);
  }
  .porch-photo {
    position: absolute;
    left: 709px;
    top: 38px;
    width: 471px;
    height: 257px;
    background: linear-gradient(180deg,
      #f4f6f7 0%, #f4f6f7 18%,
      var(--sky) 19%, #d4e6f1 45%,
      #8fae7a 50%, #a9c08c 56%,
      var(--patio) 62%, #d9cfc2 78%, var(--wicker) 100%);
  }
  .headline {
    position: absolute;
    left: 40px;
    top: 20px;
    width: 655px;
    font-family: "Anton", "Impact", sans-serif;
    font-weight: 400;
    font-size: 84px;
    line-height: 93px;
    letter-spacing: 0.3px;
    transform: scaleY(1.1);
    transform-origin: left top;
  }
  .headline-line { display: block; white-space: nowrap; }
  .headline-line--blue { color: var(--brand-blue); }
  .headline-line--green { color: var(--headline-green); }
  .brand {
    position: absolute;
    left: 41px;
    top: 250px;
    height: 56px;
    display: flex;
    align-items: center;
    gap: 14px;
  }
  .brand-square {
    width: 52px;
    height: 52px;
    background: var(--brand-blue);
  }
  .brand-name {
    font-family: "Oswald", sans-serif;
    font-weight: 500;
    font-size: 40px;
    color: var(--brand-blue);
    letter-spacing: 0.2px;
    white-space: nowrap;
  }
  .phone {
    position: absolute;
    left: 490px;
    top: 248px;
    height: 60px;
    display: flex;
    align-items: center;
    gap: 6px;
    z-index: 2;
  }
  .phone-icon { width: 44px; height: 44px; }
  .phone-number {
    font-family: "Montserrat", sans-serif;
    font-weight: 700;
    font-size: 55px;
    color: var(--deep-blue);
    white-space: nowrap;
    letter-spacing: 0.3px;
  }
</style>
</head>
<body>
  <section class="billboard">
    <div class="accent-bar"></div>
    <div class="porch-photo" role="img" aria-label="Bright screened porch with wicker lounge chairs, ceiling fan and a lake view"></div>

    <h1 class="headline">
      <span class="headline-line headline-line--blue">Screen Your Porch.</span>
      <span class="headline-line headline-line--green">Build for the Coast.</span>
    </h1>

    <div class="brand">
      <span class="brand-square"></span>
      <span class="brand-name">HARBORLINE SCREENS</span>
    </div>

    <div class="phone">
      <svg class="phone-icon" viewBox="0 0 48 48" aria-hidden="true">
        <path d="M13 7c2-1 4 0 5 2l3 6c1 2 0 4-1 5l-3 2c2 5 6 9 11 11l2-3c1-1 3-2 5-1l6 3c2 1 3 3 2 5l-2 4c-1 2-4 3-7 2C22 41 7 26 5 15c-1-3 0-6 2-7z" fill="#5bbd5f"/>
        <path d="M27 9a13 13 0 0 1 12 12" stroke="#5bbd5f" stroke-width="3.5" fill="none" stroke-linecap="round"/>
        <path d="M26 3a19 19 0 0 1 19 19" stroke="#5bbd5f" stroke-width="3.5" fill="none" stroke-linecap="round"/>
      </svg>
      <span class="phone-number">555.014.2276</span>
    </div>
  </section>
</body>
</html>
```